(Expedite) Business Card
Pacific Motor Keep
(Expedite) Business Card - Real Estate
Creative Brief
Use standard fonts
please be creative - ok to use a different font than the logo
Professional
State-of-the-Art Car Storage & Collection Management
27405 W. Lindenmoor Avenue Harbor Vale, CA 93071
info@pacificmotorkeep.com
www.pacificmotorkeep.com
Logo on front of business card, contact information on back of business card.
Contact information on back of business card.
PacificMotorKeep PacificMotorKeep

```html
<!DOCTYPE html>
<html lang="en">
<head>
<meta charset="utf-8">
<title>Pacific Motor Keep – Business Card</title>
<link href="https://fonts.googleapis.com/css2?family=Michroma&family=Open+Sans:wght@400;600&display=swap" rel="stylesheet">
<style>
  :root{
    --stage:#8d8d8d;
    --ink:#141414;
    --paper:#ffffff;
    --orange:#ec6a1e;
    --soft:#d9d9d9;
  }
  *{box-sizing:border-box;margin:0;padding:0}
  html,body{width:1200px;height:908px;overflow:hidden}
  body{background:var(--stage);font-family:"Open Sans",Arial,sans-serif;position:relative}
  .card{position:absolute;width:540px;height:309px;border-radius:16px;overflow:hidden;
        box-shadow:0 10px 28px rgba(0,0,0,.35)}
  .card-front{left:40px;top:300px;background:var(--ink)}
  .card-back{left:620px;top:300px;background:var(--paper)}

  .brand{font-family:"Michroma",Arial,sans-serif;font-weight:400;text-transform:uppercase;letter-spacing:1px;line-height:1.15}
  .front-brand{position:absolute;left:36px;top:112px;display:flex;align-items:center;gap:14px}
  .front-brand .brand{color:var(--paper);font-size:22px}
  .brand-square{width:34px;height:34px;background:var(--orange);flex:none}
  .tagline{position:absolute;left:36px;top:192px;color:var(--orange);font-size:12.5px;font-weight:600}

  .back-art{position:absolute;inset:0}
  .back-brand{position:absolute;left:28px;top:62px;display:flex;align-items:center;gap:12px}
  .back-brand .brand{color:var(--ink);font-size:17px}
  .back-brand .brand-square{width:28px;height:28px}
  .holder{position:absolute;right:26px;top:62px;text-align:right;color:var(--paper)}
  .holder-name{font-size:16px;font-weight:600;line-height:1.2}
  .holder-role{font-size:12px}
  .contact{position:absolute;left:28px;top:190px;color:var(--soft);font-size:10.5px;line-height:1.5;list-style:none}
  .contact li{display:flex;align-items:center;gap:7px}
  .contact .addr{display:block;margin-bottom:2px}
  .dot{width:10px;height:10px;border-radius:50%;background:var(--orange);flex:none;display:flex;align-items:center;justify-content:center}
  .dot svg{width:6px;height:6px}
</style>
</head>
<body>
  <section class="card card-front">
    <div class="front-brand">
      <span class="brand-square"></span>
      <span class="brand">Pacific<br>Motor Keep</span>
    </div>
    <p class="tagline">State-of-the-Art Car Storage &amp; Collection Management</p>
  </section>

  <section class="card card-back">
    <svg class="back-art" viewBox="0 0 540 309" preserveAspectRatio="none" aria-hidden="true">
      <polygon points="0,178 250,178 272,158 540,158 540,309 0,309" fill="var(--ink)"/>
      <polygon points="0,172 248,172 270,152 540,152 540,160 274,160 252,180 0,180" fill="var(--orange)"/>
      <polygon points="340,52 540,52 540,112 360,112 340,82" fill="var(--orange)"/>
    </svg>
    <div class="back-brand">
      <span class="brand-square"></span>
      <span class="brand">Pacific<br>Motor Keep</span>
    </div>
    <div class="holder">
      <p class="holder-name">Your Name</p>
      <p class="holder-role">Position</p>
    </div>
    <ul class="contact">
      <li class="addr">27405 W. Lindenmoor Avenue<br>Harbor Vale, CA 93071</li>
      <li><span class="dot"><svg viewBox="0 0 10 10"><path d="M2 1h2l1 2-1 1c.6 1.2 1.3 1.9 2.5 2.5l1-1 2 1v2c-4 .5-8-3.5-7.5-7.5z" fill="#fff"/></svg></span>(555) 555-0142</li>
      <li><span class="dot"><svg viewBox="0 0 10 10"><path d="M2 1h2l1 2-1 1c.6 1.2 1.3 1.9 2.5 2.5l1-1 2 1v2c-4 .5-8-3.5-7.5-7.5z" fill="#fff"/></svg></span>(555) 555-0187</li>
      <li><span class="dot"><svg viewBox="0 0 10 10"><rect x="1" y="2.5" width="8" height="5" fill="none" stroke="#fff"/><path d="M1 2.5l4 3 4-3" fill="none" stroke="#fff"/></svg></span>info@pacificmotorkeep.com</li>
      <li><span class="dot"></span>PacificMotorKeep</li>
      <li><span class="dot"></span>www.pacificmotorkeep.com</li>
    </ul>
  </section>
</body>
</html>
```